Progressive/contemporary business card design for successful Startups as a Service Company

New logo launched in 2020. New website launched in 2021. Now that COVID is (mostly) behind us, I'm networking with more people and need a business card that matches the company/logo design aesthetic.

```html
<!DOCTYPE html>
<html lang="en">
<head>
<meta charset="utf-8">
<title>Ridgeline Business Card</title>
<link rel="stylesheet" href="https://fonts.googleapis.com/css2?family=Oswald:wght@300;400;700&display=swap">
<style>
  :root {
    --page-bg: #e4e4e4;
    --card-bg: #f5f5f3;
    --navy: #334766;
    --grey: #8a8a8a;
    --accent: #e8402a;
  }
  * { margin: 0; padding: 0; box-sizing: border-box; }
  html, body {
    width: 1200px;
    height: 900px;
    overflow: hidden;
    background: var(--page-bg);
    font-family: "Oswald", sans-serif;
  }
  .canvas {
    position: relative;
    width: 1200px;
    height: 900px;
  }
  .card {
    position: absolute;
    left: 250px;
    width: 700px;
    height: 400px;
    background: var(--card-bg);
    box-shadow: 0 2px 6px rgba(0,0,0,0.12);
  }
  .card--back { top: 40px; }
  .card--front { top: 460px; }

  /* Back face: company name */
  .brand {
    position: absolute;
    inset: 0;
    display: flex;
    align-items: center;
    justify-content: center;
    gap: 18px;
  }
  .brand__name {
    font-weight: 400;
    font-size: 54px;
    letter-spacing: 0.3em;
    text-transform: uppercase;
    color: var(--navy);
  }
  .brand__mark {
    width: 34px;
    height: 34px;
    background: var(--accent);
  }

  /* Front face: person details */
  .person {
    position: absolute;
    left: 33px;
    top: 30px;
  }
  .person__name {
    font-weight: 700;
    font-size: 78px;
    line-height: 1;
    color: var(--navy);
  }
  .person__title {
    margin-top: 4px;
    font-weight: 300;
    font-size: 26px;
    line-height: 1.1;
    color: var(--grey);
    text-transform: uppercase;
  }
  .contact {
    position: absolute;
    left: 33px;
    bottom: 28px;
    list-style: none;
    font-weight: 300;
    font-size: 17px;
    line-height: 24px;
    color: var(--grey);
  }
  .contact__city { text-transform: uppercase; }
  .tagline {
    position: absolute;
    right: 30px;
    top: 52px;
    writing-mode: vertical-rl;
    font-weight: 300;
    font-size: 18px;
    letter-spacing: 0.04em;
    color: var(--grey);
  }
</style>
</head>
<body>
  <main class="canvas">
    <section class="card card--back" aria-label="Card back">
      <div class="brand">
        <span class="brand__name">Ridgeline</span>
        <span class="brand__mark" aria-hidden="true"></span>
      </div>
    </section>

    <section class="card card--front" aria-label="Card front">
      <div class="person">
        <h1 class="person__name">Daniel Marsh</h1>
        <p class="person__title">Executive Director</p>
      </div>
      <ul class="contact">
        <li>(312) 555-0148</li>
        <li>info@ridgelineadvisory.com</li>
        <li>www.ridgelineadvisory.com</li>
        <li class="contact__city">Chicago</li>
      </ul>
      <p class="tagline">Guiding your company boldly toward growth.</p>
    </section>
  </main>
</body>
</html>
```